Feral Horizon, a 3d voxel survival video game needs a card for gaming conventions

I am the lead developer for Feral Horizon http://www.FeralHorizon.example and need a business card to hand out at an indie gaming convention
The card would need to include the game name, website url, my name, position (Lead Developer), e-mail and phone number
The game is a 3d, voxel (with smooth terrain) based survival game with guns and wildlife. The main icon of the game would likely be a grizzly bear but I am willing to accept other designs too.
Attached is a media kit for the game with some images you can use but don't have to its just what little art I can provide. Anything on the website or from the video game can also be used. unrelated art can also be used.
Target Market(s)
Indie Developers/publishers at conferences
Industry/Entity Type
Games
Contact Information for Business Card
Name: Corwin Aldersby
Position: Lead Developer
E-mail: Pale_Lanterns@mailbox.example
Phone number: 555-207-3186

```html
<!DOCTYPE html>
<html lang="en">
<head>
<meta charset="utf-8">
<title>Feral Horizon – Business Card</title>
<link href="https://fonts.googleapis.com/css2?family=Roboto:wght@400;700;900&display=swap" rel="stylesheet">
<style>
  :root {
    --page-bg: #2b2a26;
    --card-center: #ebe8d8;
    --card-mid: #b9b596;
    --card-edge: #5f5e42;
    --brand-red: #c8392f;
    --name-red: #d9413a;
    --role-white: #ffffff;
    --contact-ink: #3b3a33;
    --bear-light: #b48357;
    --bear-dark: #5e3f27;
  }
  html, body {
    margin: 0;
    padding: 0;
    width: 1200px;
    height: 858px;
    overflow: hidden;
    background: var(--page-bg);
    font-family: "Roboto", Arial, sans-serif;
  }
  .sheet {
    position: relative;
    width: 1200px;
    height: 858px;
    display: flex;
    align-items: center;
    justify-content: center;
    gap: 40px;
  }
  .card {
    position: relative;
    width: 540px;
    height: 309px;
    border-radius: 3px;
    overflow: hidden;
    background: radial-gradient(ellipse 75% 85% at 58% 45%, var(--card-center) 0%, var(--card-mid) 55%, var(--card-edge) 100%);
    box-shadow: 0 6px 18px rgba(0,0,0,.45);
  }
  .brand-name {
    margin: 0;
    font-weight: 900;
    text-transform: uppercase;
    color: var(--brand-red);
    white-space: nowrap;
  }
  .card--front .brand-name {
    position: absolute;
    left: 30px;
    top: 36px;
    font-size: 30px;
    letter-spacing: 1px;
  }
  .bear-photo {
    position: absolute;
    right: 0;
    top: 0;
    width: 200px;
    height: 309px;
    background: linear-gradient(160deg, var(--bear-light) 0%, var(--bear-dark) 100%);
    opacity: .9;
  }
  .person {
    position: absolute;
    left: 60px;
    top: 104px;
  }
  .person-name {
    margin: 0;
    font-size: 16px;
    font-weight: 700;
    letter-spacing: 1px;
    color: var(--name-red);
  }
  .person-role {
    margin: 2px 0 0;
    font-size: 13px;
    color: var(--role-white);
    letter-spacing: .5px;
  }
  .contact {
    position: absolute;
    left: 60px;
    bottom: 26px;
    margin: 0;
    padding: 0;
    list-style: none;
    font-size: 14px;
    color: var(--contact-ink);
  }
  .contact li {
    display: flex;
    align-items: center;
    gap: 8px;
    margin-top: 6px;
    white-space: nowrap;
  }
  .contact-icon {
    width: 14px;
    height: 14px;
    flex: none;
  }
  .card--back {
    display: flex;
    align-items: center;
    justify-content: center;
  }
  .card--back .brand-name {
    font-size: 46px;
    letter-spacing: 2px;
  }
</style>
</head>
<body>
<main class="sheet">
  <section class="card card--front" aria-label="Card front">
    <div class="bear-photo" role="img" aria-label="Photograph of a brown grizzly bear walking"></div>
    <h1 class="brand-name">Feral Horizon</h1>
    <div class="person">
      <p class="person-name">Corwin Aldersby</p>
      <p class="person-role">Lead Developer</p>
    </div>
    <ul class="contact">
      <li>
        <svg class="contact-icon" viewBox="0 0 14 14" aria-hidden="true">
          <rect width="14" height="14" fill="#fff"/>
          <path d="M4 2.5 L5.8 4.6 L4.9 5.6 Q6 8 8.4 9.1 L9.4 8.2 L11.5 10 L10.4 11.5 Q5 11 2.5 3.6 Z" fill="#3b3a33"/>
        </svg>
        <span>555-207-3186</span>
      </li>
      <li>
        <svg class="contact-icon" viewBox="0 0 14 14" aria-hidden="true">
          <rect width="14" height="14" fill="#fff"/>
          <rect x="2.5" y="4" width="9" height="6.5" fill="none" stroke="#3b3a33" stroke-width="1.2"/>
          <path d="M2.5 4 L7 8 L11.5 4" fill="none" stroke="#3b3a33" stroke-width="1.2"/>
        </svg>
        <span>Pale_Lanterns@mailbox.example</span>
      </li>
      <li>
        <svg class="contact-icon" viewBox="0 0 14 14" aria-hidden="true">
          <rect width="14" height="14" fill="#fff"/>
          <circle cx="7" cy="7" r="4.5" fill="none" stroke="#3b3a33" stroke-width="1.1"/>
          <ellipse cx="7" cy="7" rx="2" ry="4.5" fill="none" stroke="#3b3a33" stroke-width="1"/>
          <path d="M2.5 7 H11.5" stroke="#3b3a33" stroke-width="1"/>
        </svg>
        <span>http://www.FeralHorizon.example</span>
      </li>
    </ul>
  </section>

  <section class="card card--back" aria-label="Card back">
    <h2 class="brand-name">Feral Horizon</h2>
  </section>
</main>
</body>
</html>
```